Business Card Design

I have two logos , one is for the front of the card and the other for the back. The front image is the road and the sun, the back image should be the atom with the motto at the bottom. The back of the card should be black with the atom and lettering white. The front should have the image with the road and lettering black with the yellow sun all on a white background.
Updates

I have changed what I would like done. The only logo I want to use is the atom logo. White lettering with a black background on the front and back of the card. There should be no contact info on the back of the card. On the back there should b the logo with company name and the slogan underneath at the bottom of the card, also on the back if you can have the logo  image in the background as well in a gray or silver can be tiled or cascade of some sort.

On the front it should have all of the contact info with an email address added  tarnvista@quellmail.net   Black background with white lettering and another larger image of the logo in a gray or silver in the background. The logo and name side by side with the slogan directly under the name.

Industry/Entity Type

Business

Contact Information for Business Card

Colin Marsh
Director of Operations
8162 Pemberly Ln #417
Georgetown, TX 78633
Cell: (512)804-3176
Fax: (512)471-0852

```html
<!DOCTYPE html>
<html lang="en">
<head>
<meta charset="utf-8">
<title>Brazos Mobile Imaging – Business Card Back</title>
<link rel="stylesheet" href="https://fonts.googleapis.com/css2?family=Questrial&display=swap">
<style>
  :root {
    --card-black: #000000;
    --tile-glow: rgba(70, 70, 70, 0.32);
    --tile-fade: rgba(70, 70, 70, 0);
    --mark-grey: #9a9a9a;
    --text-white: #ffffff;
    --text-shadow: rgba(0, 0, 0, 0.9);
  }
  html, body {
    margin: 0;
    padding: 0;
    width: 1200px;
    height: 702px;
    overflow: hidden;
    background: var(--card-black);
  }
  .card-back {
    position: relative;
    width: 1200px;
    height: 702px;
    background: var(--card-black);
    font-family: "Questrial", "Century Gothic", sans-serif;
    color: var(--text-white);
    overflow: hidden;
  }
  .tiled-backdrop {
    position: absolute;
    inset: 0;
    background-image: radial-gradient(ellipse 62px 56px at 50% 50%, var(--tile-glow) 0%, var(--tile-fade) 100%);
    background-size: 171px 153px;
    background-position: 52px 24px;
  }
  .brand-mark {
    position: absolute;
    left: 562px;
    top: 396px;
    width: 64px;
    height: 64px;
    border-radius: 50%;
    background: var(--mark-grey);
  }
  .company-name {
    position: absolute;
    left: 0;
    right: 0;
    top: 502px;
    margin: 0;
    text-align center;
    text-align: center;
    font-size: 48px;
    font-weight: 400;
    line-height: 1;
    text-shadow: 2px 2px 3px var(--text-shadow);
  }
  .slogan {
    position: absolute;
    left: 0;
    right: 0;
    top: 579px;
    margin: 0;
    text-align: center;
    font-size: 29px;
    font-weight: 400;
    line-height: 1;
  }
</style>
</head>
<body>
  <main class="card-back">
    <div class="tiled-backdrop" role="img" aria-label="Faint grey tiled pattern of the company emblem repeated across the black background"></div>
    <div class="brand-mark" aria-hidden="true"></div>
    <h1 class="company-name">Brazos Mobile Imaging</h1>
    <p class="slogan">Professional Timely Accurate</p>
  </main>
</body>
</html>
```